VORDA HOMES PELAB MARKETING FLYER

THE FLYER CAN BE FRONT TO BACK OR 2 PAGES IF NEEDED.

need to create a flyer with the following information:

Tallyworth Inc. is a CRM (Customer Relationship Management System) that provides leads to agents and a system to communicate and track your leads. Initial training and set up will be provided

Commission splits for leads are as follows: (maybe we can create a chart or box for items 1-3)

1. Cold leads 40% Vorda - 60% Agent - Worked by Agent in the platform, agent shows property, writes contract, handles all negotiations and any necessary addendums, attends home inspection and settlement.

2. Warm leads 50% Vorda - 50% Co-agent - Contacted by ISA, agent shows property, writes contract, handles all negotiations and any necessary addendums, attends home inspection and settlement.

3 Hot leads 70% Vorda - 30% Co-agent - Prequalified by Vorda Homes and ready to look at property, Vorda writes contract and secures broker agency relationship agreements, co-agent shows property, , handles all negotiations (with support from VORDA if necessary), execute any necessary addendums, attend home inspection and settlement.

Preferred vendors such as Lender, Title, Insurance, Home Inspector, etc. are to be used for any transactions related to PELB per Vorda Homes.

Agents will receive 10 leads for free to start once Fresh Broker Launchpad is complete. Warm leads will be available to purchase for $15 each beyond the first 10. Every 5 deals closed, agent commission will increase by 10% annually!!

Rules and restrictions apply.

3. In addition to Quillset, a transaction coordinator included.

4. Free PELB Support and training included

5. Free personal CRM website included

Industry/Entity Type

Real Estate

Colors
3176b5
85abd2
ecf5f6

Requirements
Must have
• everything in the description above

```html
<!DOCTYPE html>
<html lang="en">
<head>
<meta charset="utf-8">
<title>Vorda Homes · Pelab Marketing Flyer</title>
<link href="https://fonts.googleapis.com/css2?family=Josefin+Sans:wght@400;600;700&display=swap" rel="stylesheet">
<style>
  :root {
    --navy: #0f3478;
    --blue: #3176b5;
    --sky: #85abd2;
    --mist: #ecf5f6;
    --yellow: #f5e64c;
    --gray-band: #d6d6d6;
    --stage: #4a4a4a;
    --white: #ffffff;
  }
  * { box-sizing: border-box; margin: 0; padding: 0; }
  html, body { width: 965px; height: 1200px; overflow: hidden; }
  body {
    background: var(--stage);
    font-family: "Josefin Sans", Arial, sans-serif;
    color: var(--navy);
    display: flex; align-items: center; justify-content: center; gap: 25px;
  }
  .page {
    position: relative; width: 460px; height: 592px;
    background: var(--white); overflow: hidden;
  }
  /* front */
  .front-hero { position: absolute; inset: 0 0 auto 0; height: 420px;
    background: linear-gradient(160deg, #f4f6fa 0%, #dde5ef 45%, #c3cfdd 100%); }
  .front-shapes { position: absolute; left: 0; top: 0; }
  .brand {
    position: absolute; top: 408px; left: 0; right: 0;
    display: flex; align-items: center; justify-content: center; gap: 8px;
  }
  .brand-mark { width: 22px; height: 22px; background: var(--navy); }
  .brand-name { font-size: 26px; font-weight: 600; letter-spacing: 2px; color: var(--navy); }
  .front-intro {
    position: absolute; top: 472px; left: 22px; right: 22px;
    text-align: center; font-weight: 700; font-size: 14.2px; line-height: 1.27;
  }
  .contact-bar {
    position: absolute; left: 0; right: 0; bottom: 0; height: 24px;
    background: var(--gray-band);
    display: flex; align-items: center; justify-content: space-between;
    padding: 0 16px; font-size: 10px; color: var(--navy);
  }
  .contact-item { display: flex; align-items: center; gap: 5px; }
  .contact-item svg { width: 10px; height: 10px; fill: var(--navy); }
  /* back */
  .splits-title { position: absolute; top: 28px; left: 0; right: 0; text-align: center;
    font-size: 14.5px; font-weight: 700; }
  .split-grid { position: absolute; top: 58px; left: 18px; right: 18px;
    display: flex; gap: 10px; }
  .split-card { flex: 1; height: 134px; background: var(--navy); border-radius: 8px; overflow: hidden; }
  .split-head { background: var(--yellow); text-align: center; padding: 4px 2px 3px;
    border-radius: 8px 8px 0 0; }
  .split-name { font-size: 13px; font-weight: 700; color: var(--navy); }
  .split-ratio { font-size: 8.6px; font-weight: 700; color: var(--navy); }
  .split-body { color: var(--white); font-size: 7.2px; line-height: 1.45; text-align: center;
    padding: 9px 6px 0; }
  .vendors { position: absolute; top: 205px; left: 30px; right: 30px; text-align: center;
    font-size: 8.4px; line-height: 1.3; color: #222; }
  .offer { position: absolute; top: 235px; left: 26px; right: 26px; text-align: center;
    font-weight: 700; font-size: 11.3px; line-height: 1.25; color: #111; }
  .offer .hl { color: var(--blue); }
  .rules { position: absolute; top: 304px; left: 50%; transform: translateX(-50%);
    background: var(--navy); color: var(--yellow); font-weight: 700; font-size: 11.2px;
    padding: 5px 14px 3px; border-radius: 12px; white-space: nowrap; }
  .perks { position: absolute; top: 339px; left: 0; right: 0; list-style: none; text-align: center;
    font-size: 8.6px; line-height: 1.85; color: #222; }
  .team-photo { position: absolute; top: 392px; left: 20px; right: 20px; height: 162px;
    background: linear-gradient(180deg, #f3f3f3 0%, #5b5f68 35%, #2b2e35 70%, #eeeeee 100%); }
  .partner-banner { position: absolute; top: 448px; left: 40px; right: 40px; height: 56px;
    background: var(--white); display: flex; align-items: center; justify-content: space-around;
    box-shadow: 0 1px 3px rgba(0,0,0,.25); }
  .partner { font-size: 17px; font-weight: 600; color: var(--navy); letter-spacing: 1px;
    display: flex; align-items: center; gap: 5px; }
  .partner-square { width: 14px; height: 14px; background: var(--navy); }
  .partner-badge { width: 44px; height: 26px; background: var(--sky); }
</style>
</head>
<body>
  <section class="page page-front">
    <div class="front-hero" role="img" aria-label="Businessman's hand drawing CRM sketch icons: cloud, target, chat bubble, chart, bulb, globe and envelope"></div>
    <svg class="front-shapes" width="460" height="592" viewBox="0 0 460 592">
      <polygon points="240,345 460,255 460,392" fill="var(--navy)"/>
      <polygon points="0,396 240,345 460,392 460,592 0,592" fill="var(--white)"/>
    </svg>
    <div class="brand"><span class="brand-mark"></span><span class="brand-name">VORDA</span></div>
    <p class="front-intro">Tallyworth Inc. is a CRM (Customer Relationship Management System) that provides leads to agents and a system to communicate and track your leads. Initial training and set up will be provided</p>
    <footer class="contact-bar">
      <span class="contact-item"><svg viewBox="0 0 10 10"><path d="M2 0h2l1 3-1.5 1a6 6 0 0 0 2.5 2.5L7 5l3 1v2a2 2 0 0 1-2 2A8 8 0 0 1 0 2a2 2 0 0 1 2-2z"/></svg>+1 555-014-2288</span>
      <span class="contact-item"><svg viewBox="0 0 10 10"><path d="M0 2h10v6H0zM0 2l5 3 5-3v1L5 6 0 3z" fill-rule="evenodd"/></svg>info@vordahomes.net</span>
      <span class="contact-item"><svg viewBox="0 0 10 10"><circle cx="5" cy="5" r="5"/></svg>www.vordahomes.net</span>
    </footer>
  </section>

  <section class="page page-back">
    <h2 class="splits-title">Commission splits for leads are as follows:</h2>
    <div class="split-grid">
      <article class="split-card">
        <header class="split-head"><div class="split-name">Cold leads</div><div class="split-ratio">40% Vorda - 60% Agent</div></header>
        <p class="split-body">Worked by Agent in the platform, agent shows property, writes contract, handles all negotiations and any necessary addendums, attends home inspection and settlement.</p>
      </article>
      <article class="split-card">
        <header class="split-head"><div class="split-name">Warm leads</div><div class="split-ratio">50% Vorda - 50% Co-agent</div></header>
        <p class="split-body">Contacted by ISA, agent shows property, writes contract, handles all negotiations and any necessary addendums, attends home inspection and settlement.</p>
      </article>
      <article class="split-card">
        <header class="split-head"><div class="split-name">Hot leads</div><div class="split-ratio">70% Vorda - 30% Co-agent</div></header>
        <p class="split-body" style="font-size:6.5px;padding-top:5px;line-height:1.4">Prequalified by Vorda Homes and ready to look at property, Vorda writes contract and secures broker agency relationship agreements, co-agent shows property, , handles all negotiations (with support from VORDA if necessary), execute any necessary addendums, attend home inspection and settlement.</p>
      </article>
    </div>
    <p class="vendors">Preferred vendors such as Lender, Title, Insurance, Home Inspector, etc. are to be used for any transactions related to PELB per Vorda Homes.</p>
    <p class="offer">Agents will receive <span class="hl">10 leads for free to start</span> once Fresh Broker Launchpad is complete. Warm leads will be available to purchase for <span class="hl">$15</span> each beyond the first 10. Every 5 deals closed, agent commission will increase by <span class="hl">10% annually!!</span></p>
    <div class="rules">Rules and restrictions apply.</div>
    <ul class="perks">
      <li>3. In addition to Quillset, a transaction coordinator included.</li>
      <li>4. Free PELB Support and training included</li>
      <li>5. Free personal CRM website included</li>
    </ul>
    <div class="team-photo" role="img" aria-label="Large group of business professionals standing together holding a banner"></div>
    <div class="partner-banner">
      <span class="partner"><span class="partner-square"></span>VORDA</span>
      <span class="partner">PELB</span>
      <span class="partner-badge"></span>
    </div>
    <footer class="contact-bar">
      <span class="contact-item"><svg viewBox="0 0 10 10"><path d="M2 0h2l1 3-1.5 1a6 6 0 0 0 2.5 2.5L7 5l3 1v2a2 2 0 0 1-2 2A8 8 0 0 1 0 2a2 2 0 0 1 2-2z"/></svg>+1 555-014-2288</span>
      <span class="contact-item"><svg viewBox="0 0 10 10"><path d="M0 2h10v6H0zM0 2l5 3 5-3v1L5 6 0 3z" fill-rule="evenodd"/></svg>info@vordahomes.net</span>
      <span class="contact-item"><svg viewBox="0 0 10 10"><circle cx="5" cy="5" r="5"/></svg>www.vordahomes.net</span>
    </footer>
  </section>
</body>
</html>
```